Criação de Embalagem (unidade) para Educação & Cursos
A empresa queria:
" Levar Soluções financeira inteligente para sociedade, por meio de cursos, treinamentos e site "

```html
<!DOCTYPE html>
<html lang="pt-BR">
<head>
<meta charset="UTF-8">
<title>Box Finanças Pessoais — Embalagem</title>
<link rel="stylesheet" href="https://fonts.googleapis.com/css2?family=Montserrat:wght@500;600;700;800;900&display=swap">
<style>
  :root {
    --page-bg: #e9ecef;
    --navy-deep: #0a1240;
    --navy: #12206a;
    --blue: #1f3fa8;
    --blue-bright: #2f5fd0;
    --white: #ffffff;
    --soft-white: #dfe6ff;
  }
  * { margin: 0; padding: 0; box-sizing: border-box; }
  html, body {
    width: 1200px; height: 1200px; overflow: hidden;
    background: var(--page-bg);
    font-family: "Montserrat", sans-serif;
  }
  .canvas {
    width: 1200px; height: 1200px;
    display: flex; align-items: center; justify-content: center;
  }
  .box-face {
    position: relative;
    width: 700px; height: 1040px;
    background: var(--navy-deep);
    color: var(--white);
    overflow: hidden;
  }
  .word-cloud {
    position: absolute; inset: 0;
    background:
      repeating-linear-gradient(180deg, rgba(47,95,208,.16) 0 34px, transparent 34px 52px, rgba(31,63,168,.22) 52px 96px, transparent 96px 118px),
      repeating-linear-gradient(90deg, rgba(10,18,64,.35) 0 60px, transparent 60px 150px, rgba(10,18,64,.2) 150px 190px, transparent 190px 260px),
      radial-gradient(ellipse at 30% 95%, rgba(47,95,208,.6), transparent 60%),
      radial-gradient(ellipse at 85% 60%, rgba(31,63,168,.5), transparent 55%),
      linear-gradient(180deg, var(--navy) 0%, var(--navy-deep) 40%, #0d1a5a 100%);
  }
  .title {
    position: absolute; left: 60px; top: 70px;
    font-weight: 800; font-size: 64px; line-height: 84px;
    letter-spacing: 1px; text-transform: uppercase;
  }
  .contents {
    position: absolute; left: 418px; top: 175px;
    list-style: none;
    font-weight: 800; font-size: 21px; line-height: 39px;
    letter-spacing: 1.5px; text-transform: uppercase;
  }
  .contents li::before {
    content: ""; display: inline-block;
    width: 7px; height: 7px; border-radius: 50%;
    background: var(--white); margin-right: 8px; vertical-align: middle;
  }
  .brand {
    position: absolute; left: 190px; top: 550px;
    display: flex; align-items: flex-start; gap: 18px;
  }
  .brand-mark {
    width: 84px; height: 84px; background: var(--white); margin-top: 4px;
  }
  .brand-name {
    font-weight: 700; font-size: 30px; line-height: 34px;
  }
  .contact {
    position: absolute;
    display: flex; align-items: center; gap: 8px;
    font-weight: 500; font-size: 16px; color: var(--soft-white);
    white-space: nowrap;
  }
  .contact svg { width: 20px; height: 20px; flex: none; }
  .dot { width: 16px; height: 16px; border-radius: 50%; border: 2px solid var(--soft-white); flex: none; }
  .contact-phone { left: 80px; top: 705px; }
  .contact-social { left: 270px; top: 705px; }
  .contact-email { left: 120px; top: 778px; font-size: 14px; }
  .contact-page { left: 385px; top: 776px; font-size: 14px; }
  .website {
    position: absolute; left: 0; right: 0; top: 812px; text-align: center;
    font-weight: 600; font-size: 36px; letter-spacing: 1px;
  }
  .website strong { font-weight: 800; }
</style>
</head>
<body>
<main class="canvas">
  <section class="box-face">
    <div class="word-cloud" role="img" aria-label="Nuvem de palavras sobre finanças em tons de azul: liberdade, investimento, aposentadoria, riqueza, renda, seguro, lucro"></div>

    <h1 class="title">Box<br>Finança<br>Pessoais</h1>

    <ul class="contents">
      <li>5 livros</li>
      <li>1 ebook</li>
      <li>7 ferramentas</li>
      <li>5 bônus</li>
      <li>4 material</li>
      <li>personalizado</li>
    </ul>

    <div class="brand">
      <span class="brand-mark" aria-hidden="true"></span>
      <p class="brand-name">Instituto<br>Saber<br>Financeiro</p>
    </div>

    <p class="contact contact-phone">
      <svg viewBox="0 0 24 24" aria-hidden="true"><path fill="#dfe6ff" d="M6.6 10.8a15 15 0 0 0 6.6 6.6l2.2-2.2a1 1 0 0 1 1-.25 11.4 11.4 0 0 0 3.6.57 1 1 0 0 1 1 1V20a1 1 0 0 1-1 1A17 17 0 0 1 3 4a1 1 0 0 1 1-1h3.5a1 1 0 0 1 1 1c0 1.25.2 2.45.57 3.57a1 1 0 0 1-.25 1z"/></svg>
      (11) 4000-12345
    </p>
    <p class="contact contact-social"><span class="dot"></span>@isf_financas</p>
    <p class="contact contact-email">contato@saberfinanceiro.com</p>
    <p class="contact contact-page"><span class="dot"></span>/Instituto Saber Financeiro</p>

    <p class="website">www.<strong>lucasandrade</strong>.com.br</p>
  </section>
</main>
</body>
</html>
```